Willowmere Loft B&B Business Card

This beautiful high-class B&B is looking for a business card that stands out from the rest. They are in the middle of the countryside, have chickens, geese and a dog. They also love bumble bees.

I was maybe thinking a rustic drawing / print of a bumble bee and a sketch of the house, I am not sure.. I quite like the feel of this... http://www.tarnwick-mill.co.uk/

Industry/Entity Type

Business

Contact Information for Business Card

Willowmere Loft
Bed & Breakfast
Brackleford, Hensworth, Somerset, TA14 7QP
01632 960418 | www.willowmereloft.co.uk

```html
<!DOCTYPE html>
<html lang="en">
<head>
<meta charset="utf-8">
<title>Willowmere Loft B&amp;B – Business Card</title>
<link rel="stylesheet" href="https://fonts.googleapis.com/css2?family=Libre+Baskerville:wght@400;700&family=Ubuntu:wght@300;400&display=swap">
<style>
  :root {
    --stage: #161616;
    --card: #232323;
    --card-edge: #1b1b1b;
    --panel: rgba(28,28,28,0.96);
    --ink: #f2f2f2;
    --ink-soft: #bdbdbd;
    --rule: #8a8a8a;
    --sky: #8fb6de;
    --cloud: #dfe6ee;
    --roof: #c4553a;
    --stone: #cdbb8c;
    --lawn: #4f7a2e;
    --gravel: #c9b68a;
  }
  * { box-sizing: border-box; margin: 0; padding: 0; }
  html, body {
    width: 1200px; height: 902px; overflow: hidden;
    background: var(--stage);
  }
  .stage {
    width: 1200px; height: 902px;
    display: flex; flex-direction: column;
    align-items: center; justify-content: center; gap: 44px;
  }
  .card {
    position: relative;
    width: 580px; height: 331px;
    background: radial-gradient(ellipse at 40% 35%, #2c2c2c 0%, var(--card) 55%, var(--card-edge) 100%);
    overflow: hidden;
    box-shadow: 0 18px 40px rgba(0,0,0,0.55);
  }

  /* Front */
  .photo { position: absolute; top: 0; bottom: 0; }
  .photo--left {
    left: 0; width: 176px;
    background: linear-gradient(180deg, var(--sky) 0%, var(--cloud) 18%, var(--roof) 34%, var(--stone) 48%, #9a9a5a 70%, var(--lawn) 100%);
  }
  .photo--right {
    right: 0; width: 176px;
    background: linear-gradient(180deg, var(--sky) 0%, var(--roof) 16%, var(--stone) 32%, #b8a577 65%, var(--gravel) 88%, var(--lawn) 100%);
  }
  .front-panel {
    position: absolute; left: 176px; right: 176px; top: 0; bottom: 0;
    background: var(--panel);
    display: flex; flex-direction: column; align-items: center;
    padding-top: 112px;
  }
  .brand-name {
    font-family: "Libre Baskerville", serif; font-weight: 700;
    color: var(--ink); text-transform: uppercase; letter-spacing: 0.5px;
    white-space: nowrap;
  }
  .brand-tag {
    font-family: "Libre Baskerville", serif; font-weight: 400;
    color: var(--ink-soft); text-transform: uppercase; white-space: nowrap;
  }
  .front-panel .brand-name { font-size: 13px; letter-spacing: 0.3px; }
  .front-panel .brand-tag { font-size: 8px; letter-spacing: 3px; margin-top: 5px; }
  .front-panel .site {
    position: absolute; bottom: 54px;
    font-family: "Ubuntu", sans-serif; font-weight: 300;
    font-size: 12px; color: var(--ink-soft); letter-spacing: 0.3px;
    white-space: nowrap;
  }

  /* Back */
  .back-brand {
    position: absolute; left: 40px; top: 120px; width: 250px;
    text-align: center;
  }
  .back-brand .brand-name { font-size: 19px; }
  .back-brand .brand-tag { font-size: 10.5px; letter-spacing: 4px; margin-top: 6px; }
  .divider {
    position: absolute; left: 300px; top: 112px; width: 1px; height: 62px;
    background: var(--rule);
  }
  .contact {
    position: absolute; left: 326px; top: 112px;
    font-family: "Ubuntu", sans-serif; font-weight: 400;
    font-size: 14px; line-height: 21px; color: var(--ink);
    list-style: none;
  }
  .contact li { display: flex; align-items: flex-start; gap: 10px; }
  .contact svg { flex: none; margin-top: 3px; }
  .contact .addr { font-size: 13.5px; }
  .base-rule {
    position: absolute; left: 0; bottom: 58px; width: 300px; height: 1px;
    background: linear-gradient(90deg, transparent, var(--rule));
  }
  .back .site {
    position: absolute; left: 316px; bottom: 50px;
    font-family: "Ubuntu", sans-serif; font-weight: 300;
    font-size: 14px; color: var(--ink-soft); letter-spacing: 0.4px;
  }
</style>
</head>
<body>
<main class="stage">
  <section class="card front">
    <div class="photo photo--left" role="img" aria-label="Photo of the stone barn with arched window, red tiled roof and garden lawn"></div>
    <div class="front-panel">
      <div class="brand-name">Willowmere Loft</div>
      <div class="brand-tag">Bed &amp; Breakfast</div>
      <div class="site">www.willowmereloft.co.uk</div>
    </div>
    <div class="photo photo--right" role="img" aria-label="Photo of the stone barn gable end with a wooden gate and gravel drive"></div>
  </section>

  <section class="card back">
    <div class="back-brand">
      <div class="brand-name">Willowmere Loft</div>
      <div class="brand-tag">Bed &amp; Breakfast</div>
    </div>
    <div class="divider"></div>
    <ul class="contact">
      <li>
        <svg width="14" height="14" viewBox="0 0 24 24" aria-hidden="true"><path fill="#d8d8d8" d="M6.6 10.8a15.1 15.1 0 0 0 6.6 6.6l2.2-2.2a1 1 0 0 1 1-.25 11.4 11.4 0 0 0 3.6.57 1 1 0 0 1 1 1V20a1 1 0 0 1-1 1A17 17 0 0 1 3 4a1 1 0 0 1 1-1h3.5a1 1 0 0 1 1 1c0 1.250.2 2.450.57 3.57a1 1 0 0 1-.25 1z"/></svg>
        <span>01632 960418</span>
      </li>
      <li class="addr">
        <svg width="14" height="16" viewBox="0 0 24 28" aria-hidden="true"><path fill="#d8d8d8" d="M12 0a10 10 0 0 0-10 10c0 7.5 10 18 10 18s10-10.5 10-18A10 10 0 0 0 12 0zm0 14a4 4 0 1 1 0-8 4 4 0 0 1 0 8z"/></svg>
        <span>Brackleford, Hensworth,<br>Somerset, TA14 7QP</span>
      </li>
    </ul>
    <div class="base-rule"></div>
    <div class="site">www.willowmereloft.co.uk</div>
  </section>
</main>
</body>
</html>
```